AMAZING FLYERS, POSTCARDS, AND MARKETING!!!! - Northgable Shingle & Eave Works, LLC

This project will be for Northgable Shingle & Eave Works, LLC. The flyers and postcards will be used to saturate the Alaska market with our services, and get our name and logo out there for people to remember. We plan to send the flyers and postcards out in a broad scale (both door to door and mail out). We want to send out flyers to realty and property management businesses to introduce our roofing company, and to advertise our services. We would also like to have another version, or the ability to edit the text of the final product to send out the same materials to residential clients (homeowners) by just changing the text slightly to better fit that market.
We have a logo, but need something put together that we can tri-fold and mail out to potential clients. We are planning to do some postcards as well. We would like the option to mail them or bring them to people in person.
We are a locally owned roofing and repair company in Alaska. We would like something professional that will capture their attention and show the potential of working with our company. I included some detailed information about our company and some pictures below of our work trailer and a before/after on a recent project. I also attached our logo files. Please go through the attached data and let us know what you come up with to stir up the marketing aspect of our company. Thank you for your time and consideration.

Project Deadline Extended
Reason: Allowing additional time for designers to submit/resubmit their flyer/postcard ideas based on inquiries and feedback.

Target Market(s)

1.) Homeowners are the first target market.
2.)Realtors and Property Management companies are the second market

Industry/Entity Type

Marketing

Contact Information for Business Card

Include the logo and contact information for our company. These business cards will be for the Owner, Harold Vemstrup, II.
There is also a Co-Owner, Wanda Vemstrup, so we will need the ability to print business cards for each owner. Need to be able to change the title/name and phone number for Wanda's contact information please. Contact information, license #, and logo information on one side of the card. Please tell the potential client a little about us on the back of the card by utilizing the attached information.

Requirements
Must have
• Pertinent information about our company and listed in the company information attachment. Attention getting details and design work. Professional in appearance and unique to our company to set us above the general advertisers in this industry.
Nice to have
• Something that sets our flyers apart from the ones people get every day. We want to rise above normal with our advertising.
Should not have
• Nothing plain and boring.

```html
<!DOCTYPE html>
<html lang="en">
<head>
<meta charset="utf-8">
<title>Northgable Shingle &amp; Eave Works — Postcard</title>
<link href="https://fonts.googleapis.com/css2?family=Anton&family=Open+Sans:wght@400;600;700&family=Roboto+Condensed:wght@400;700&family=Titillium+Web:ital,wght@1,700&display=swap" rel="stylesheet">
<style>
  :root {
    --ink: #0b0b0b;
    --red: #e0222a;
    --deep-red: #a3161c;
    --white: #ffffff;
    --paper: #ffffff;
    --rule: #8a8a8a;
    --backdrop: #e9e6e1;
  }
  * { box-sizing: border-box; margin: 0; padding: 0; }
  html, body { width: 1200px; height: 1200px; overflow: hidden; background: var(--backdrop); }
  .sheet {
    position: absolute; left: 228px; top: 18px;
    width: 930px; height: 1455px;
    transform: scale(0.8); transform-origin: 0 0;
    font-family: "Open Sans", sans-serif;
  }
  /* FRONT */
  .front { position: absolute; left: 0; top: 0; width: 930px; height: 719px; background: var(--ink); overflow: hidden; }
  .front-art { position: absolute; left: 0; top: 0; width: 930px; height: 562px; }
  .brand-name {
    position: absolute; left: 40px; top: 62px; width: 300px;
    color: var(--white); font-weight: 700; font-size: 26px; line-height: 1.2;
    display: flex; align-items: center; gap: 14px;
  }
  .brand-name::before { content: ""; flex: none; width: 22px; height: 22px; background: var(--red); }
  .tagline {
    position: absolute; right: 36px; top: 28px; text-align: right;
    color: var(--white); font-family: "Titillium Web", sans-serif; font-style: italic; font-weight: 700;
    line-height: 1.1;
  }
  .tagline small { display: block; font-size: 20px; }
  .tagline strong { display: block; font-size: 31px; }
  .perks { position: absolute; left: 64px; top: 430px; list-style: none; color: var(--white); font-size: 21px; line-height: 35px; }
  .perks li { display: flex; align-items: center; gap: 8px; }
  .perks svg { width: 20px; height: 20px; }
  .contact-band { position: absolute; left: 0; top: 566px; width: 930px; height: 153px; background: var(--ink); }
  .phone-icon { position: absolute; left: 58px; top: 32px; width: 72px; height: 72px; }
  .quote-label { position: absolute; left: 167px; top: 30px; color: var(--white); font-size: 21px; letter-spacing: .3px; white-space: nowrap; }
  .quote-label b { font-weight: 700; }
  .quote-number { position: absolute; left: 155px; top: 58px; color: var(--red); font-family: "Anton", sans-serif; font-size: 56px; line-height: 1; letter-spacing: -.5px; white-space: nowrap; }
  .hat-icon { position: absolute; left: 488px; top: 44px; width: 94px; height: 64px; }
  .experience { position: absolute; left: 584px; top: 28px; width: 300px; text-align: center; color: var(--white); white-space: nowrap; }
  .experience .owned { font-size: 19px; font-variant: small-caps; }
  .experience .decades { color: var(--red); font-family: "Anton", sans-serif; font-size: 42px; line-height: 1.05; }
  .experience .industry { font-size: 20px; }
  /* BACK */
  .back { position: absolute; left: 0; top: 737px; width: 930px; height: 718px; background: var(--paper); overflow: hidden; }
  .intro-panel { position: absolute; left: 0; top: 0; width: 476px; height: 718px; background: var(--ink); }
  .intro-copy { position: absolute; left: 50px; top: 37px; width: 369px; color: var(--white); font-size: 16.4px; line-height: 22.6px; text-align: justify; }
  .intro-copy.closing { top: 454px; width: 232px; }
  .intro-copy em { font-style: normal; color: var(--red); font-weight: 700; }
  .email { position: absolute; left: 50px; top: 652px; display: flex; align-items: center; gap: 14px; color: var(--white); font-size: 19px; white-space: nowrap; }
  .email svg { width: 26px; height: 18px; }
  .trailer-photo { position: absolute; left: 300px; top: 463px; width: 316px; height: 220px; }
  .postage { position: absolute; left: 762px; top: 33px; width: 135px; height: 160px; border: 2px solid var(--rule); display: flex; align-items: center; justify-content: center; text-align: center; font-size: 16px; line-height: 22px; color: #222; }
  .address-line { position: absolute; left: 527px; width: 354px; height: 0; border-top: 1.5px solid var(--rule); }
  .legal { position: absolute; right: 45px; top: 620px; text-align: right; font-family: "Roboto Condensed", sans-serif; color: var(--ink); }
  .legal .company { font-size: 16px; }
  .legal .license { font-size: 25px; font-weight: 700; line-height: 1.3; }
</style>
</head>
<body>
<main class="sheet">
  <section class="front">
    <svg class="front-art" viewBox="0 0 930 562" role="img" aria-label="Photo of a newly shingled grey roof with red house walls and trees, cut into diagonal panels">
      <defs>
        <linearGradient id="roof" x1="0" y1="0" x2="1" y2="1">
          <stop offset="0" stop-color="#6d6f70"/><stop offset="1" stop-color="#3e3f42"/>
        </linearGradient>
        <linearGradient id="redwall" x1="0" y1="0" x2="0" y2="1">
          <stop offset="0" stop-color="#c4282e"/><stop offset="1" stop-color="#7e1015"/>
        </linearGradient>
      </defs>
      <rect width="930" height="562" fill="url(#roof)"/>
      <polygon points="0,150 195,288 0,420" fill="#5d7252"/>
      <polygon points="520,0 930,0 930,330 700,120" fill="url(#redwall)" opacity=".9"/>
      <polygon points="0,420 195,288 420,562 0,562" fill="url(#redwall)"/>
      <polygon points="0,0 520,0 195,288 0,150" fill="#0b0b0b"/>
    </svg>
    <div class="brand-name">Northgable Shingle &amp; Eave Works, LLC</div>
    <p class="tagline"><small>GIVING PEACE OF MIND TO ALASKANS,</small><strong>ONE ROOF AT A TIME</strong></p>
    <ul class="perks">
      <li><svg viewBox="0 0 20 20"><path d="M2 11 L7 17 L18 3" stroke="#fff" stroke-width="2.4" fill="none"/></svg>Detail oriented</li>
      <li><svg viewBox="0 0 20 20"><path d="M2 11 L7 17 L18 3" stroke="#fff" stroke-width="2.4" fill="none"/></svg>Bonded and insured</li>
      <li><svg viewBox="0 0 20 20"><path d="M2 11 L7 17 L18 3" stroke="#fff" stroke-width="2.4" fill="none"/></svg>100% satisfaction guaranteed</li>
    </ul>
    <div class="contact-band">
      <svg class="phone-icon" viewBox="0 0 72 72" aria-hidden="true">
        <path d="M14 4 C6 8 4 18 10 30 C18 46 30 58 46 64 C56 68 64 64 68 58 L56 46 C52 44 50 46 46 50 C38 46 28 36 24 28 C28 24 30 22 28 18 Z" fill="#fff"/>
      </svg>
      <p class="quote-label"><b>FREE QUOTE</b> CALL OR TEXT</p>
      <p class="quote-number">907-555-0142</p>
      <svg class="hat-icon" viewBox="0 0 94 64" aria-hidden="true">
        <path d="M10 46 C10 18 30 6 48 6 C68 6 82 20 82 46 Z" fill="#fff"/>
        <path d="M2 46 H92 V54 C92 58 88 60 84 60 H10 C6 60 2 58 2 54 Z" fill="#d9d9d9"/>
      </svg>
      <div class="experience">
        <p class="owned">Locally Owned and Operated</p>
        <p class="decades">Over 2 Decades</p>
        <p class="industry">in the roofing &amp; repair industry</p>
      </div>
    </div>
  </section>

  <section class="back">
    <div class="intro-panel">
      <p class="intro-copy">We’ve been working in the nearby area and would like to introduce ourselves. <em>Northgable Shingle &amp; Eave Works, LLC</em> is a local business, owned and operated by people born and raised right here in Alaska. We love our state and the sense of community that is uniquely Alaskan, and strive to give our clients the best service possible. With over two decades of experience in the roofing and repair industry, we would appreciate the opportunity to interview to be your roofing company of choice. Our focus is on quality work for residential client and property management companies and finding the right service that will best fit their needs. We offer free estimates for small repairs as well as full roof replacements and would be happy to assist you if you would like to contact us with any questions. Our goal is to</p>
      <p class="intro-copy closing">be Alaska’s premier residential roofing and repair company and provide quality workmanship to our friends and neighbors. Thank you for your time and have a wonderful day!</p>
      <p class="email"><svg viewBox="0 0 26 18" aria-hidden="true"><rect width="26" height="18" rx="2" fill="#fff"/><path d="M1 2 L13 11 L25 2" stroke="#0b0b0b" stroke-width="2" fill="none"/></svg>hi@northgable.com</p>
    </div>
    <svg class="trailer-photo" viewBox="0 0 316 220" role="img" aria-label="Photo of the company's black enclosed work trailer with ladders on the roof rack">
      <rect width="316" height="220" fill="#1a1a1a"/>
      <rect width="316" height="40" fill="#5a5a5a" opacity=".6"/>
    </svg>
    <div class="postage">Postage<br>Area</div>
    <div class="address-line" style="top:281px"></div>
    <div class="address-line" style="top:349px"></div>
    <div class="address-line" style="top:417px"></div>
    <div class="legal">
      <p class="company">Northgable Shingle &amp; Eave Works, LLC</p>
      <p class="license">License #2287</p>
    </div>
  </section>
</main>
</body>
</html>
```